Home Security Company Business Card

Looking for a eye catching business card that is non traditional and stands out but yet still looks professional. It should include all the pertinent information such as name, title, address, telephone, e-mail, website address should definitely stand out and then finally the logo.

Target Market(s)

Residential and Commercial accounts mostly upscale accounts

Industry/Entity Type

Security

Contact Information for Business Card

Name
Title
Address
Office #
Cell #
E-mail
Website

Font styles to use
Serif
Sans Serif

Requirements
Must have
• Logo, two sided color configuration
Nice to have
• You decide
Should not have
• There really aren't any.

```html
<!DOCTYPE html>
<html lang="en">
<head>
<meta charset="utf-8">
<title>Kestrel Security Systems – Business Card</title>
<link href="https://fonts.googleapis.com/css2?family=Tinos:wght@400;700&family=Noto+Serif:wght@400&display=swap" rel="stylesheet">
<style>
  :root {
    --maroon: #7b1518;
    --gold: #e3b448;
    --white: #ffffff;
    --backdrop: #f2e6cf;
    --rule: #a8474a;
  }
  * { margin: 0; padding: 0; box-sizing: border-box; }
  html, body { width: 1189px; height: 1200px; overflow: hidden; background: var(--backdrop); }
  .canvas { position: relative; width: 1189px; height: 1200px; }
  .card { position: absolute; left: 171px; width: 856px; height: 486px; border-radius: 20px; overflow: hidden; }
  .card--front { top: 69px; background: var(--maroon); }
  .card--back { top: 627px; background: var(--white); }
  .abs { position: absolute; line-height: 1; white-space: nowrap; }

  .brand-mark { position: absolute; border-radius: 50%; background: var(--gold); }
  .front-mark { left: 86px; top: 132px; width: 190px; height: 190px; }
  .back-mark { left: 182px; top: 150px; width: 96px; height: 96px; }

  .brand { font-family: "Tinos", serif; font-weight: 400; }
  .brand-name { font-size: 57px; letter-spacing: -0.5px; }
  .brand-sub { font-size: 24px; letter-spacing: -0.3px; }
  .card--front .brand { color: var(--white); }
  .card--back .brand { color: var(--maroon); }

  .front-web { right: 48px; top: 434px; font-family: "Noto Serif", serif; font-size: 21px; color: var(--white); letter-spacing: 0.8px; }

  .divider { position: absolute; left: 423px; top: 95px; width: 1px; height: 291px; background: var(--rule); }

  .contact { font-family: "Noto Serif", serif; color: var(--maroon); }
  .person-name { left: 464px; top: 102px; font-size: 32px; }
  .person-title { left: 464px; top: 136px; font-size: 20px; color: var(--gold); letter-spacing: 0.5px; }
  .address { left: 464px; top: 184px; font-size: 22px; line-height: 29px; white-space: pre; }
  .row { left: 464px; display: flex; align-items: center; gap: 16px; font-size: 21px; }
  .row svg { width: 23px; height: 23px; flex: none; }
  .row--office { top: 251px; }
  .row--cell { top: 282px; }
  .row--mail { top: 313px; }
  .web { left: 464px; top: 361px; font-size: 21px; color: var(--gold); letter-spacing: 0.8px; }
</style>
</head>
<body>
<main class="canvas">

  <section class="card card--front" aria-label="Card front">
    <div class="brand-mark front-mark"></div>
    <div class="abs brand brand-name" style="left:329px; top:200px;">KESTREL</div>
    <div class="abs brand brand-sub" style="left:329px; top:257px;">SECURITY SYSTEMS INC.</div>
    <div class="abs front-web">www.kestrelsecure.com</div>
  </section>

  <section class="card card--back" aria-label="Card back">
    <div class="brand-mark back-mark"></div>
    <div class="abs brand brand-name" style="left:119px; top:300px; width:224px; text-align:center; font-size:50px;">KESTREL</div>
    <div class="abs brand brand-sub" style="left:109px; top:350px; width:244px; text-align:center; font-size:22px;">SECURITY SYSTEMS INC.</div>

    <div class="divider"></div>

    <div class="abs contact person-name">Dana Whitfield</div>
    <div class="abs contact person-title">Owner</div>
    <div class="abs contact address">PO Box 4410 Alder Way
Spokane, WA 99201 USA</div>

    <div class="abs contact row row--office">
      <svg viewBox="0 0 24 24" aria-hidden="true"><rect width="24" height="24" rx="4" fill="var(--gold)"/><path d="M6 10c0-3 12-3 12 0v1h-3v-1.5h-6V11H6z M8 12h8l1 6H7z" fill="#fff"/></svg>
      <span>555-014-2290</span>
    </div>
    <div class="abs contact row row--cell">
      <svg viewBox="0 0 24 24" aria-hidden="true"><rect width="24" height="24" rx="4" fill="var(--gold)"/><rect x="8" y="4" width="8" height="16" rx="1.5" fill="none" stroke="#fff" stroke-width="1.6"/><rect x="10" y="7" width="4" height="4" fill="#fff"/></svg>
      <span>+1 555-014-2291</span>
    </div>
    <div class="abs contact row row--mail">
      <svg viewBox="0 0 24 24" aria-hidden="true"><rect width="24" height="24" rx="4" fill="var(--gold)"/><rect x="5" y="7" width="14" height="10" fill="none" stroke="#fff" stroke-width="1.6"/><path d="M5 7l7 6 7-6M5 17l5-5M19 17l-5-5" fill="none" stroke="#fff" stroke-width="1.4"/></svg>
      <span>hello@kestrelsecure.com</span>
    </div>

    <div class="abs contact web">www.kestrelsecure.com</div>
  </section>

</main>
</body>
</html>
```